Corvane Holdings , new business card design

investment firm with corporate clients . need double sided business card , vertical and horizontal options ,logo must be clear. prefer pantone colors only and sharp design. website also www.corvane-example.ae

Khalid Bin Rashed
Managing Director
Tel. +971 4 000 3829
Mobile +971 50 000 4172
khalid@corvane-example.ae
Palm Crest Tower, officw 18-B07, Qasr Gardens, Dubai

Contact Information for Business Card

Khalid Bin Rashed
Managing Director

Font styles to use
Serif

Colors

Designer to choose colors to be used in the design.

```html
<!DOCTYPE html>
<html lang="en">
<head>
<meta charset="utf-8">
<title>Corvane Holdings – Business Card</title>
<link href="https://fonts.googleapis.com/css2?family=Josefin+Sans:wght@300&family=Open+Sans:wght@400;600;700&display=swap" rel="stylesheet">
<style>
  :root{
    --page:#e8e9ec;
    --card-white:#f7f7f7;
    --brand-blue:#4a73a0;
    --brand-blue-dark:#3f6894;
    --stripe-grey:#c9c6c2;
    --ink:#2c2f35;
    --ink-soft:#55585e;
    --on-blue:#ffffff;
  }
  *{margin:0;padding:0;box-sizing:border-box}
  html,body{width:1200px;height:900px;overflow:hidden}
  body{background:var(--page);font-family:"Open Sans",Arial,sans-serif;position:relative}

  .card{position:absolute;width:560px;height:320px;border-radius:18px;overflow:hidden;
        box-shadow:0 10px 28px rgba(0,0,0,.18)}
  .card--front{left:320px;top:95px;background:var(--card-white)}
  .card--back{left:320px;top:485px;background:var(--brand-blue)}

  .card__shapes{position:absolute;inset:0;width:560px;height:320px}

  .brand-name{position:absolute;font-family:"Josefin Sans",Arial,sans-serif;font-weight:300;
              text-transform:uppercase;letter-spacing:.32em;white-space:nowrap}
  .card--front .brand-name{left:0;right:0;top:52px;text-align:center;font-size:30px;color:var(--ink)}
  .card--back .brand-name{left:0;right:0;top:140px;text-align:center;font-size:32px;color:var(--on-blue)}

  .holder{position:absolute;left:200px;top:112px;text-align:center;width:260px}
  .holder__name{font-weight:700;font-size:17px;color:var(--brand-blue);text-transform:uppercase;letter-spacing:.01em}
  .holder__title{font-size:13px;color:var(--ink-soft);margin-top:2px}

  .contact{position:absolute;color:var(--on-blue);font-size:12.5px;line-height:1.45;white-space:nowrap}
  .contact b{font-weight:700}
  .contact--phone{left:30px;top:262px}
  .contact--web{left:180px;width:200px;top:212px;text-align:center}
  .contact--address{left:372px;width:172px;top:160px;text-align:center;font-size:12px}

  .world-area{position:absolute;left:40px;top:40px;width:480px;height:240px;border-radius:40px;
              background:radial-gradient(ellipse at center,rgba(255,255,255,.16),rgba(255,255,255,0) 70%)}
</style>
</head>
<body>

<section class="card card--front" aria-label="Business card front">
  <svg class="card__shapes" viewBox="0 0 560 320" aria-hidden="true">
    <polygon points="0,230 560,112 560,122 0,240" fill="var(--stripe-grey)"/>
    <polygon points="0,240 560,122 560,320 0,320" fill="var(--brand-blue)"/>
    <!-- phone icon -->
    <g transform="translate(110,212)">
      <circle r="11" fill="var(--stripe-grey)"/>
      <path d="M-5,-4 q0,9 9,9 l2,-2 -3,-2 -1.5,1.5 q-3,-1 -4,-4 l1.5,-1.5 -2,-3z" fill="#fff"/>
    </g>
    <!-- globe icon -->
    <g transform="translate(280,176)">
      <circle r="11" fill="var(--stripe-grey)"/>
      <g fill="none" stroke="#fff" stroke-width="1.2">
        <circle r="6"/><ellipse rx="2.6" ry="6"/><line x1="-6" y1="0" x2="6" y2="0"/>
      </g>
    </g>
    <!-- pin icon -->
    <g transform="translate(460,139)">
      <circle r="11" fill="var(--stripe-grey)"/>
      <path d="M0,7 C-3,2 -5,0 -5,-2 A5,5 0 0 1 5,-2 C5,0 3,2 0,7z" fill="#fff"/>
      <circle cy="-2" r="1.8" fill="var(--stripe-grey)"/>
    </g>
  </svg>

  <div class="brand-name">Corvane Holdings</div>

  <div class="holder">
    <div class="holder__name">Khalid Bin Rashed</div>
    <div class="holder__title">Managing Director</div>
  </div>

  <div class="contact contact--phone">
    <div><b>T:</b> +971 4 000 3829</div>
    <div><b>P:</b> +971 50 000 4172</div>
  </div>
  <div class="contact contact--web">
    <div>khalid@corvane-example.ae</div>
    <div>www.corvane-example.ae</div>
  </div>
  <div class="contact contact--address">
    <div>Palm Crest Tower, officw 18-B07,</div>
    <div>Qasr Gardens, Dubai</div>
  </div>
</section>

<section class="card card--back" aria-label="Business card back">
  <div class="world-area" role="img" aria-label="Faint dotted world map in lighter blue"></div>
  <div class="brand-name">Corvane Holdings</div>
</section>

</body>
</html>
```